Torvale Wound Care Business card design

We need a business card designed around our logo which was provided. The logo of preference is the colored. Also the colors and fonts were provided.

Target Market(s)

Our Referral partners are home health agencies.

Industry/Entity Type

Healthcare

Contact Information for Business Card

Name , Phone #, Email , Title

Requirements
Nice to have
• Creativity
Should not have
• basic

```html
<!DOCTYPE html>
<html lang="en">
<head>
<meta charset="utf-8">
<title>Torvale Wound Care — Business Card</title>
<link href="https://fonts.googleapis.com/css2?family=Marcellus&display=swap" rel="stylesheet">
<style>
  :root{
    --page:#e9ebee;
    --navy:#0d3f86;
    --blue-deep:#0b4a8f;
    --blue-mid:#1375bd;
    --blue-light:#1fa5df;
    --sky:#2a9ad6;
    --ink:#2b3440;
    --card-white:#ffffff;
    --card-grey:#ececee;
  }
  html,body{margin:0;padding:0;width:1200px;height:900px;overflow:hidden;background:var(--page);}
  body{font-family:"Marcellus",Georgia,serif;color:var(--ink);}
  .stage{position:relative;width:1200px;height:900px;}
  .card{
    position:absolute;left:320px;width:560px;height:320px;border-radius:26px;
    box-shadow:0 10px 28px rgba(20,40,70,.22);overflow:hidden;
  }
  .card--front{top:80px;background:linear-gradient(115deg,var(--blue-deep) 0%,var(--blue-mid) 55%,var(--blue-light) 100%);}
  .card--back{top:480px;background:linear-gradient(120deg,var(--card-grey) 0%,var(--card-white) 70%);}

  .brand{display:flex;align-items:center;gap:14px;white-space:nowrap;}
  .brand__dot{width:22px;height:22px;border-radius:50%;flex:none;}
  .brand__name{font-size:40px;line-height:1;letter-spacing:.5px;}
  .card--front .brand{position:absolute;left:50%;top:50%;transform:translate(-50%,-50%);}
  .card--front .brand__dot{background:#fff;}
  .card--front .brand__name{color:#fff;}

  .person{position:absolute;left:34px;top:150px;}
  .person__name{font-size:22px;letter-spacing:1px;color:var(--navy);text-transform:uppercase;margin:0;font-weight:400;}
  .person__title{font-size:15px;color:var(--ink);margin:4px 0 0;}

  .contact{position:absolute;left:300px;top:34px;list-style:none;margin:0;padding:0;font-size:14px;line-height:22px;}
  .contact li{display:flex;align-items:center;gap:8px;}
  .contact svg{width:14px;height:14px;fill:var(--navy);flex:none;}
  .area{position:absolute;left:322px;top:128px;font-size:14px;line-height:20px;margin:0;}
  .rule{position:absolute;left:322px;top:178px;width:206px;height:1px;background:var(--sky);}
  .card--back .brand{position:absolute;right:30px;bottom:46px;}
  .card--back .brand__dot{background:var(--navy);}
  .card--back .brand__name{color:var(--navy);font-size:36px;}
</style>
</head>
<body>
<main class="stage">
  <section class="card card--front" aria-label="Card front">
    <div class="brand">
      <span class="brand__dot"></span>
      <span class="brand__name">Torvale Wound Care</span>
    </div>
  </section>

  <section class="card card--back" aria-label="Card back">
    <div class="person">
      <h1 class="person__name">Dana Whitfield</h1>
      <p class="person__title">Managing Director</p>
    </div>

    <ul class="contact">
      <li><svg viewBox="0 0 24 24"><path d="M6.6 10.8a15.1 15.1 0 0 0 6.6 6.6l2.2-2.2a1 1 0 0 1 1-.25 11.4 11.4 0 0 0 3.6.57 1 1 0 0 1 1 1V20a1 1 0 0 1-1 1A17 17 0 0 1 3 4a1 1 0 0 1 1-1h3.5a1 1 0 0 1 1 1c0 1.250.2 2.45.57 3.57a1 1 0 0 1-.25 1z"/></svg>404-555-0172</li>
      <li><svg viewBox="0 0 24 24"><path d="M6 2h12v5H6zM4 8h16a2 2 0 0 1 2 2v7h-4v5H6v-5H2v-7a2 2 0 0 1 2-2zm4 8v4h8v-4z"/></svg>404-555-0139</li>
      <li><svg viewBox="0 0 24 24"><path d="M2 5h20v14H2zm2 2v.5l8 5 8-5V7zm0 3v7h16v-7l-8 5z"/></svg>info@torvalecare.com</li>
      <li><svg viewBox="0 0 24 24"><path d="M12 2a10 10 0 1 0 0 20 10 10 0 0 0 0-20zm6.9 9h-3a15 15 0 0 0-1.3-5.6A8 8 0 0 1 18.9 11zM12 4c.9 1.2 1.7 3.6 1.9 7h-3.8c.2-3.4 1-5.8 1.9-7zM9.4 5.4A15 15 0 0 0 8.1 11h-3a8 8 0 0 1 4.3-5.6zM5.1 13h3a15 15 0 0 0 1.3 5.6A8 8 0 0 1 5.1 13zM12 20c-.9-1.2-1.700-3.6-1.9-7h3.8c-.2 3.4-1 5.8-1.9 7zm2.6-1.4a15 15 0 0 0 1.3-5.6h3a8 8 0 0 1-4.3 5.6z"/></svg>www.torvalecare.com</li>
    </ul>
    <p class="area">Serving Harlan, Brookdale<br>Marlow &amp; Ashby Counties, VT</p>
    <div class="rule"></div>

    <div class="brand">
      <span class="brand__dot"></span>
      <span class="brand__name">Torvale Wound Care</span>
    </div>
  </section>
</main>
</body>
</html>
```